Harbor of Mercy - Team of Rabbis and Doctors Helping Families Dealing with Illness

The Harbor of Mercy is an organization that accompanies families dealing with severe illnesses of a family member. A team of rabbis and doctors provide support and real-time responses to these families.
The site theme is medicine and law, but the target market is religious Jewish families in crisis. Thus, the site design needs to combine:
- professional, conservative, serious
- spiritual
- warm hug

Target Market(s)

religious families suffering a health crisis

Industry/Entity Type

Non-profit organization

Number of Pages Required

1 page

Font styles to use
Sans Serif

Requirements
Must have
• Final design in PSD format. List of fonts used, colors used and link/button colors used in the design.

```html
<!DOCTYPE html>
<html lang="en">
<head>
<meta charset="utf-8">
<title>Harbor of Mercy</title>
<link href="https://fonts.googleapis.com/css2?family=Montserrat:wght@400;500;600;700;800&family=Mulish:wght@400;600;700&family=Roboto+Slab:wght@300;700&display=swap" rel="stylesheet">
<style>
:root{
  --navy:#211e74;
  --navy-dark:#1a175f;
  --gold:#d8b20c;
  --gold-soft:#e8c93a;
  --orange:#e8a23a;
  --cream:#f8f4e3;
  --cream-light:#fbf8ee;
  --text:#2b2b3a;
  --muted:#55566a;
  --white:#ffffff;
}
*{box-sizing:border-box;margin:0;padding:0}
html,body{width:1200px;height:4528px;overflow:hidden;background:var(--white)}
body{position:relative;font-family:"Mulish",sans-serif;color:var(--text)}
.abs{position:absolute}
h1,h2,h3,h4{font-family:"Montserrat",sans-serif}
.title{font-size:32px;font-weight:700;color:var(--navy);line-height:1}
.title span{color:var(--gold)}
.underline{text-decoration:underline;text-decoration-color:var(--navy);text-underline-offset:6px;text-decoration-thickness:2px}
.btn{position:absolute;display:flex;align-items:center;justify-content:center;border-radius:20px;font-family:"Montserrat",sans-serif;font-weight:600;font-size:11px;letter-spacing:.3px;text-transform:uppercase}
.btn-navy{background:var(--navy);color:var(--white)}
.btn-gold{background:var(--gold);color:var(--white)}
p{font-size:11.5px;line-height:1.75;color:var(--muted)}
.photo{position:absolute}

/* top bar */
.topbar{left:0;top:0;width:1200px;height:63px;background:var(--navy)}
.search{left:141px;top:13px;width:170px;height:37px;border:1.5px solid #fff;border-radius:20px;color:#fff;font-size:11px;padding:11px 20px}
.top-item{top:13px;height:37px;display:flex;align-items:center;gap:10px;color:#fff;font-size:11.5px}
.ring{width:30px;height:30px;border:1.5px solid #fff;border-radius:50%;display:flex;align-items:center;justify-content:center}
.dedic{top:14px;height:36px;font-size:11px;text-transform:uppercase}
/* nav */
.nav{top:63px;left:0;width:1200px;height:92px;background:#fff}
.nav a{position:absolute;top:38px;font-size:11.5px;color:var(--text);text-decoration:none}
.nav a.active{color:var(--navy);font-weight:700}
.wordmark{font-family:"Montserrat",sans-serif;font-weight:800;color:var(--gold);font-size:23px;line-height:1.05;text-align:right}
/* hero */
.hero{left:0;top:155px;width:1200px;height:543px;background:linear-gradient(90deg,#e9e8e6 0%,#d8d3cc 45%,#b8aa9a 75%,#8f8579 100%)}
.hero h1{font-family:"Roboto Slab",serif;font-weight:300;font-size:42px;line-height:51px;color:#1c1b22;left:158px;top:150px}
.hero h1 b{font-weight:700}
.hero-bar{left:141px;top:163px;width:4px;height:134px;background:var(--orange)}
.hero-phone{left:141px;top:333px;width:212px;height:42px;border-radius:22px;background:var(--navy);color:#fff;font-family:"Montserrat",sans-serif;font-weight:700;font-size:18px;letter-spacing:1px;display:flex;align-items:center;gap:14px;padding-left:6px}
.hero-phone i{width:32px;height:32px;border-radius:50%;background:#fff;display:flex;align-items:center;justify-content:center}
.dots{left:572px;top:500px;display:flex;gap:8px}
.dots i{width:7px;height:7px;border-radius:50%;background:#fff;opacity:.7}
.dots i:first-child{background:var(--orange);opacity:1}
/* service cards */
.card{position:absolute;width:209px;height:292px;background:var(--gold);border-radius:8px;overflow:hidden}
.card .pic{height:137px}
.card h4{font-size:14px;color:var(--navy);margin:26px 21px 8px;font-weight:700}
.card p{color:#fff;font-size:11px;line-height:1.6;margin:0 21px}
.more{font-family:"Montserrat",sans-serif;font-size:11px;font-weight:700;display:flex;align-items:center;gap:8px}
.card .more{color:var(--navy);margin:8px 21px}
/* reviews */
.review{position:absolute;width:286px;height:253px;background:#fff;border-radius:8px;box-shadow:0 4px 18px rgba(0,0,0,.06);padding:30px 26px}
.avatar{width:46px;height:46px;border-radius:50%;background:#c9bfb6}
.review h4{font-size:11px;margin:22px 0 20px;font-weight:700}
.review p{font-size:11px;color:var(--text)}
.arrow{position:absolute;width:36px;height:36px;border-radius:50%;display:flex;align-items:center;justify-content:center}
/* news */
.news{position:absolute;top:2948px;width:286px;height:382px;background:var(--cream-light);border-radius:10px;overflow:hidden}
.news .pic{height:177px;border-radius:10px}
.news .body{padding:22px 28px}
.news small{font-size:11px;color:var(--text)}
.news h4{font-size:12px;line-height:1.7;margin:8px 0 10px;color:var(--text)}
.news p{font-size:11px;line-height:1.6;color:var(--muted)}
.news .more{color:var(--text);margin-top:18px}
/* footer */
.footer h3{font-size:14px;color:var(--gold);font-weight:700;text-transform:uppercase}
.f-line{display:flex;gap:12px;color:#fff;font-size:11px;line-height:1.6;align-items:flex-start}
.qlinks a{display:block;color:#fff;font-size:11px;text-decoration:none;margin-bottom:13px}
</style>
</head>
<body>

<!-- Top bar -->
<div class="abs topbar"></div>
<div class="abs search">Search
  <svg class="abs" style="right:16px;top:10px" width="16" height="16" viewBox="0 0 16 16"><circle cx="6.5" cy="6.5" r="5" fill="none" stroke="#fff" stroke-width="2"/><path d="M10.5 10.5L15 15" stroke="#fff" stroke-width="2"/></svg>
</div>
<div class="abs top-item" style="left:338px"><span class="ring"><svg width="8" height="8"><rect width="8" height="8" rx="4" fill="#fff"/></svg></span></div>
<div class="abs top-item" style="left:395px"><span class="ring"><svg width="14" height="10" viewBox="0 0 14 10"><rect x=".75" y=".75" width="12.5" height="8.5" rx="1" fill="none" stroke="#fff" stroke-width="1.5"/><path d="M1 1l6 5 6-5" fill="none" stroke="#fff" stroke-width="1.5"/></svg></span>info@harborofmercy.org</div>
<div class="abs top-item" style="left:601px"><span class="ring"><svg width="13" height="13" viewBox="0 0 24 24"><path fill="#fff" d="M6.6 10.8a15 15 0 006.6 6.6l2.2-2.2c.3-.3.7-.4 1-.2 1.1.4 2.3.6 3.6.6.6 0 1 .4 1 1V20c0 .6-.4 1-1 1C10.6 21 3 13.4 3 4c0-.6.4-1 1-1h3.5c.6 0 1 .4 1 1 0 1.3.2 2.5.6 3.6.1.3 0 .7-.2 1z"/></svg></span>123 456 7890</div>
<div class="btn dedic" style="left:789px;width:130px;border:1.5px solid var(--gold);color:#fff">Dedication 2</div>
<div class="btn dedic" style="left:933px;width:126px;background:var(--gold);color:#fff">Dedication 1</div>

<!-- Nav -->
<div class="abs nav">
  <a class="active" style="left:141px">Home</a>
  <a style="left:216px">About Us</a>
  <a style="left:309px">Courses</a>
  <a style="left:395px">Conferences</a>
  <a style="left:506px">Lectures</a>
  <a style="left:587px">News</a>
  <a style="left:661px">Contact Us</a>
  <div class="abs wordmark" style="left:873px;top:22px;width:187px">Harbor<br>of Mercy</div>
</div>

<!-- Hero -->
<div class="abs hero" role="img" aria-label="Photo of a visitor reading a book to a smiling patient in a hospital bed"></div>
<div class="abs hero-bar"></div>
<h1 class="abs" style="font-family:'Roboto Slab',serif;font-weight:300;font-size:42px;line-height:51px;color:#1c1b22;left:158px;top:305px">Should cancer<br>patients <b>continue<br>treatment?</b></h1>
<div class="abs hero-phone" style="top:488px"><i><svg width="16" height="16" viewBox="0 0 24 24"><path fill="#211e74" d="M6.6 10.8a15 15 0 006.6 6.6l2.2-2.2c.3-.3.7-.4 1-.2 1.1.4 2.3.6 3.6.6.6 0 1 .4 1 1V20c0 .6-.4 1-1 1C10.6 21 3 13.4 3 4c0-.6.4-1 1-1h3.5c.6 0 1 .4 1 1 0 1.3.2 2.5.6 3.6.1.3 0 .7-.2 1z"/></svg></i>123 456 7890</div>
<div class="abs dots" style="top:653px"><i></i><i></i><i></i><i></i></div>

<!-- About -->
<div class="photo" style="left:0;top:761px;width:557px;height:414px;border-radius:0 18px 18px 0;background:radial-gradient(circle at 55% 45%,#8a6a2a 0%,#3a2a14 45%,#15110c 100%)" role="img" aria-label="Photo of hands opening a book beside a lit menorah with gifts and a dreidel"></div>
<svg class="abs" style="left:236px;top:926px" width="84" height="84" viewBox="0 0 84 84"><circle cx="42" cy="42" r="39" fill="none" stroke="#fff" stroke-width="4"/><path d="M33 26l26 16-26 16z" fill="#fff"/></svg>
<h2 class="abs title underline" style="left:643px;top:833px">About <span>Us</span></h2>
<p class="abs" style="left:643px;top:888px;width:420px;color:var(--text);font-weight:700;font-size:11.5px;line-height:1.75">The Harbor of Mercy is an organization that accompanies families dealing with severe illnesses of a family member. A team of rabbis and doctors provide support and real-time responses to these families.</p>
<p class="abs" style="left:643px;top:956px;width:420px">Lorem ipsum dolor sit amet, consectetur adipiscing elit, sed do eiusmod tempor incididunt ut labore et dolore magna aliqua. Ut enim ad minim veniam, quis nostrud exercitation ullamco laboris nisi ut aliquip ex ea commodo consequat.</p>
<div class="btn btn-navy" style="left:643px;top:1068px;width:119px;height:32px">Learn More</div>

<!-- Moral issues -->
<div class="abs" style="left:0;top:1402px;width:1200px;height:360px;background:var(--navy)"></div>
<div class="abs" style="left:141px;top:1291px;width:102px;height:109px;background:var(--navy);opacity:.95;border-radius:0 0 50px 50px/0 0 40px 40px" role="img" aria-label="Menorah icon"></div>
<h2 class="abs title" style="left:144px;top:1478px;color:var(--gold);font-size:32px">More Moral <span style="color:#fff">Issues</span></h2>
<p class="abs" style="left:141px;top:1526px;width:410px;color:#fff">Lorem ipsum dolor sit amet, consectetur adipiscing elit, sed do eiusmod tempor incididunt ut labore et dolore magna aliqua. Ut enim ad minim veniam, quis nostrud exercitation ullamco laboris nisi ut aliquip ex ea commodo consequat.</p>
<div class="btn btn-gold" style="left:141px;top:1644px;width:123px;height:35px">Contact Us</div>
<div class="abs" style="left:631px;top:1262px;width:437px;height:425px;background:#fff;border-radius:18px;box-shadow:0 8px 24px rgba(0,0,0,.12)"></div>
<div class="photo" style="left:643px;top:1262px;width:416px;height:413px;border-radius:16px;background:radial-gradient(circle at 30% 80%,#c88a34 0%,#4a3a2e 35%,#24211f 100%)" role="img" aria-label="Photo of a man in a kippah lighting a menorah"></div>

<!-- Service cards -->
<div class="card" style="left:141px;top:1848px"><div class="pic" style="background:linear-gradient(135deg,#4b4a47,#1f1e1c)" role="img" aria-label="Photo of a man studying a book"></div><h4>Courses</h4><p>Lorem ipsum dolor sit amet, consectetur adipiscing elit, sed do eiusmod tempor.</p><div class="more">Learn More <svg width="16" height="8"><path d="M0 4h14M10 1l4 3-4 3" fill="none" stroke="#211e74" stroke-width="1.5"/></svg></div></div>
<div class="card" style="left:376px;top:1891px"><div class="pic" style="background:linear-gradient(135deg,#6b5d52,#2a2522)" role="img" aria-label="Photo of a group meeting around a table"></div><h4>Conferences</h4><p>Lorem ipsum dolor sit amet, consectetur adipiscing elit, sed do eiusmod tempor.</p><div class="more">Learn More <svg width="16" height="8"><path d="M0 4h14M10 1l4 3-4 3" fill="none" stroke="#211e74" stroke-width="1.5"/></svg></div></div>
<div class="card" style="left:611px;top:1848px"><div class="pic" style="background:linear-gradient(135deg,#8a6a3c,#2b1f14)" role="img" aria-label="Photo of an audience at a lecture"></div><h4>Lectures</h4><p>Lorem ipsum dolor sit amet, consectetur adipiscing elit, sed do eiusmod tempor.</p><div class="more">Learn More <svg width="16" height="8"><path d="M0 4h14M10 1l4 3-4 3" fill="none" stroke="#211e74" stroke-width="1.5"/></svg></div></div>
<div class="card" style="left:849px;top:1891px"><div class="pic" style="background:linear-gradient(135deg,#d9dcdf,#8c8f92)" role="img" aria-label="Photo of a hotline operator with a headset at a computer"></div><h4>Hotline 24/7</h4><p>Lorem ipsum dolor sit amet, consectetur adipiscing elit, sed do eiusmod tempor.</p><div class="more">Learn More <svg width="16" height="8"><path d="M0 4h14M10 1l4 3-4 3" fill="none" stroke="#211e74" stroke-width="1.5"/></svg></div></div>

<!-- Reviews -->
<div class="abs" style="left:0;top:2268px;width:1200px;height:534px;background:var(--cream)"></div>
<h2 class="abs title underline" style="left:0;width:1200px;text-align:center;top:2343px">Our Customers <span>Review</span></h2>
<div class="arrow" style="left:77px;top:2561px;border:1.5px solid var(--gold)"><svg width="10" height="12"><path d="M8 1L2 6l6 5" fill="none" stroke="#211e74" stroke-width="2"/></svg></div>
<div class="arrow" style="left:1087px;top:2561px;background:var(--navy)"><svg width="10" height="12"><path d="M2 1l6 5-6 5" fill="none" stroke="#fff" stroke-width="2"/></svg></div>
<div class="review" style="left:141px;top:2462px"><div class="avatar" role="img" aria-label="Customer portrait"></div><h4>Lorem ipsum</h4><p>Standard dummy text ever since the 1500s, when an unknown printer took a galley of type and scrambled it to make a type specimen book. It has survived not only five centuries.</p></div>
<div class="review" style="left:457px;top:2419px"><div class="avatar" role="img" aria-label="Customer portrait"></div><h4>Lorem ipsum</h4><p>Standard dummy text ever since the 1500s, when an unknown printer took a galley of type and scrambled it to make a type specimen book. It has survived not only five centuries.</p></div>
<div class="review" style="left:773px;top:2462px"><div class="avatar" role="img" aria-label="Customer portrait"></div><h4>Lorem ipsum</h4><p>Standard dummy text ever since the 1500s, when an unknown printer took a galley of type and scrambled it to make a type specimen book. It has survived not only five centuries.</p></div>

<!-- News -->
<h2 class="abs title underline" style="left:141px;top:2878px">News <span>Feeds</span></h2>
<div class="news" style="left:141px"><div class="pic" style="background:linear-gradient(180deg,#c9b08a,#8f7550)" role="img" aria-label="Photo of people praying at a stone wall"></div><div class="body"><small>02 Nov, 2023</small><h4>Lorem ipsum dolor sit amet, consectetur adipiscing.</h4><p>Ut enim ad minim veniam, quis nostrud exercitation ullamco laboris nisi ut aliquip ex ea commodo consequat.</p><div class="more">Learn More <svg width="16" height="8"><path d="M0 4h14M10 1l4 3-4 3" fill="none" stroke="#2b2b3a" stroke-width="1.5"/></svg></div></div></div>
<div class="news" style="left:457px"><div class="pic" style="background:linear-gradient(135deg,#a46a3a,#5a3518)" role="img" aria-label="Photo of hands holding a card with a star symbol on wood"></div><div class="body"><small>02 Nov, 2023</small><h4>Lorem ipsum dolor sit amet, consectetur adipiscing.</h4><p>Ut enim ad minim veniam, quis nostrud exercitation ullamco laboris nisi ut aliquip ex ea commodo consequat.</p><div class="more">Learn More <svg width="16" height="8"><path d="M0 4h14M10 1l4 3-4 3" fill="none" stroke="#2b2b3a" stroke-width="1.5"/></svg></div></div></div>
<div class="news" style="left:773px"><div class="pic" style="background:radial-gradient(circle at 75% 60%,#c98a3a,#3a2a1c 60%,#1b1510)" role="img" aria-label="Photo of a couple lighting candles"></div><div class="body"><small>02 Nov, 2023</small><h4>Lorem ipsum dolor sit amet, consectetur adipiscing.</h4><p>Ut enim ad minim veniam, quis nostrud exercitation ullamco laboris nisi ut aliquip ex ea commodo consequat.</p><div class="more">Learn More <svg width="16" height="8"><path d="M0 4h14M10 1l4 3-4 3" fill="none" stroke="#2b2b3a" stroke-width="1.5"/></svg></div></div></div>

<!-- Contact -->
<div class="abs" style="left:0;top:3418px;width:1200px;height:486px;background:var(--cream)"></div>
<div class="abs" style="left:188px;top:3505px;width:824px;height:313px;background:#fff;border-radius:16px;overflow:hidden">
  <div class="abs" style="left:0;top:0;width:369px;height:313px;background:linear-gradient(135deg,#2a2780,#1a175f)" role="img" aria-label="Dark navy panel over a candle photo"></div>
  <h3 class="abs" style="left:42px;top:40px;color:#fff;font-size:15px;font-weight:600">CONTACT DETAILS</h3>
  <div class="abs" style="left:42px;top:62px;width:54px;height:2px;background:var(--gold)"></div>
  <div class="abs f-line" style="left:42px;top:86px;width:260px"><svg width="32" height="32"><circle cx="16" cy="16" r="16" fill="#fff"/><path d="M16 8a5 5 0 00-5 5c0 4 5 10 5 10s5-6 5-10a5 5 0 00-5-5z" fill="#d8b20c"/><circle cx="16" cy="13" r="2" fill="#fff"/></svg><span>123, Ut enim ad minim veniam, quis nostrud exercitation ullamco laboris nisi ut aliquip.</span></div>
  <div class="abs f-line" style="left:42px;top:155px;align-items:center;font-weight:700"><svg width="32" height="32"><circle cx="16" cy="16" r="16" fill="#fff"/><path transform="translate(9 9) scale(.6)" fill="#d8b20c" d="M6.6 10.8a15 15 0 006.6 6.6l2.2-2.2c.3-.3.7-.4 1-.2 1.1.4 2.3.6 3.6.6.6 0 1 .4 1 1V20c0 .6-.4 1-1 1C10.6 21 3 13.4 3 4c0-.6.4-1 1-1h3.5c.6 0 1 .4 1 1 0 1.3.2 2.5.6 3.6.1.3 0 .7-.2 1z"/></svg>123 456 7890</div>
  <div class="abs f-line" style="left:42px;top:213px;align-items:center"><svg width="32" height="32"><circle cx="16" cy="16" r="16" fill="#fff"/><rect x="9" y="11" width="14" height="10" rx="1" fill="none" stroke="#d8b20c" stroke-width="1.5"/><path d="M9 12l7 5 7-5" fill="none" stroke="#d8b20c" stroke-width="1.5"/></svg>info@harborofmercy.org</div>
  <h2 class="abs" style="left:411px;top:36px;width:380px;font-size:32px;line-height:42px;color:var(--navy);font-weight:700">Lorem ipsum dolor sit amet, consectetur adipiscing elit, sed do eiusmod tempor.</h2>
  <div class="btn btn-navy" style="left:411px;top:253px;width:134px;height:35px">Ask the Rabbi</div>
</div>

<!-- Newsletter + footer -->
<div class="abs" style="left:0;top:4096px;width:1200px;height:432px;background:var(--navy)"></div>
<div class="abs" style="left:141px;top:3988px;width:918px;height:141px;background:var(--gold);border-radius:22px"></div>
<h2 class="abs" style="left:211px;top:4023px;font-size:30px;line-height:40px;color:var(--navy);font-weight:800">SUBSCRIBE<br>TO NEWSLETTER</h2>
<div class="abs" style="left:546px;top:4036px;width:443px;height:39px;background:#fff;border-radius:22px;font-size:10px;color:#666;padding:13px 26px">Enter Your Email Address*</div>
<div class="btn btn-navy" style="left:877px;top:4039px;width:110px;height:33px">Subscribe</div>

<div class="footer">
  <h3 class="abs" style="left:142px;top:4213px">Contact Details</h3>
  <div class="abs f-line" style="left:142px;top:4244px;width:230px"><svg width="14" height="16" viewBox="0 0 14 16"><path d="M7 0a6 6 0 00-6 6c0 4.5 6 10 6 10s6-5.5 6-10a6 6 0 00-6-6z" fill="#fff"/><circle cx="7" cy="6" r="2" fill="#211e74"/></svg><span>123, Ut enim ad minim veniam, quis nostrud exercitation ullamco laboris nisi ut aliquip.</span></div>
  <div class="abs f-line" style="left:142px;top:4312px;align-items:center;font-weight:700"><svg width="14" height="14" viewBox="0 0 24 24"><path fill="#fff" d="M6.6 10.8a15 15 0 006.6 6.6l2.2-2.2c.3-.3.7-.4 1-.2 1.1.4 2.3.6 3.6.6.6 0 1 .4 1 1V20c0 .6-.4 1-1 1C10.6 21 3 13.4 3 4c0-.6.4-1 1-1h3.5c.6 0 1 .4 1 1 0 1.3.2 2.5.6 3.6.1.3 0 .7-.2 1z"/></svg>123 456 7890</div>
  <div class="abs f-line" style="left:142px;top:4346px;align-items:center"><svg width="14" height="11" viewBox="0 0 14 11"><rect x=".75" y=".75" width="12.5" height="9.5" rx="1" fill="none" stroke="#fff" stroke-width="1.5"/><path d="M1 1l6 5 6-5" fill="none" stroke="#fff" stroke-width="1.5"/></svg>info@harborofmercy.org</div>

  <h3 class="abs" style="left:541px;top:4213px">Quick Links</h3>
  <div class="abs qlinks" style="left:541px;top:4250px"><a style="font-weight:700">Home</a><a>About Us</a><a>Courses</a><a>Conferences</a><a>Lectures</a><a>News</a><a>Contact Us</a></div>

  <div class="abs wordmark" style="left:800px;top:4222px;width:254px;text-align:center;font-size:26px">Harbor<br>of Mercy</div>
  <div class="abs f-line" style="left:884px;top:4328px;align-items:center"><svg width="26" height="26"><circle cx="13" cy="13" r="13" fill="#d8b20c"/></svg>Community Page</div>
</div>
<div class="abs" style="left:141px;top:4490px;width:918px;height:1px;background:rgba(255,255,255,.25)"></div>
<div class="abs" style="left:0;top:4500px;width:1200px;text-align:center;color:#d8d7ea;font-size:10.5px">© 2023 The Harbor of Mercy. All Rights Reserved.</div>

</body>
</html>
```